Clay Sparrow- Hand made fashion accessories

Clay sparrow is a new business that will be selling hand made fashion accessories for women such as bags, baskets, knecklaces etc. The items are all hand made from Africa. I would like natural colors leaning more to the cardboard rustic look. I would like the card to look simple but elegant at the same time.

Industry/Entity Type

Business

Contact Information for Business Card

www.claysparrow-example.com.au
sales@claysparrow-example.com.au
Tel: 0452867310

Font styles to use
Decorative
Script

Requirements
Must have
• Earthy and rustic colours. Straw, cardboard etc. Fine black cursive print. One side of card only name
• second side website, email and tel.
Should not have
• No need to have any description of what business sells or does. No pictures of anything.

```html
<!DOCTYPE html>
<html lang="en">
<head>
<meta charset="utf-8">
<title>Clay Sparrow – Business Card</title>
<link rel="stylesheet" href="https://fonts.googleapis.com/css2?family=Great+Vibes&family=Open+Sans:wght@400;600&display=swap">
<style>
  :root {
    --canvas-bg: #efece6;
    --kraft: #c8a472;
    --kraft-light: #d6b98b;
    --kraft-dark: #a9824f;
    --straw: #e2c477;
    --bark: #5b3f22;
    --ink: #17130f;
  }
  * { box-sizing: border-box; margin: 0; padding: 0; }
  html, body {
    width: 1200px;
    height: 844px;
    overflow: hidden;
    background: var(--canvas-bg);
    font-family: "Open Sans", Arial, sans-serif;
  }
  .stage {
    width: 1200px;
    height: 844px;
    display: flex;
    align-items: center;
    justify-content: center;
    gap: 60px;
  }
  .card {
    position: relative;
    width: 520px;
    height: 300px;
    background:
      radial-gradient(ellipse at 30% 40%, var(--kraft-light), var(--kraft) 60%, var(--kraft-dark) 120%);
    overflow: hidden;
    box-shadow: 0 10px 28px rgba(60, 40, 20, 0.25);
  }
  .card__band {
    position: absolute;
    left: 0;
    right: 0;
    height: 9px;
    background: var(--bark);
  }
  .card__band--top { top: 0; }
  .card__band--bottom { top: 262px; }
  .card__jewellery {
    position: absolute;
    top: 16px;
    right: 14px;
    width: 170px;
    height: 236px;
    border-radius: 40% 30% 45% 35%;
    background:
      radial-gradient(ellipse at 65% 65%, rgba(226, 196, 119, 0.7), rgba(226, 196, 119, 0.2) 45%, rgba(200, 164, 114, 0) 70%);
  }
  .card__name {
    position: absolute;
    left: 56px;
    top: 128px;
    font-family: "Great Vibes", cursive;
    font-weight: 400;
    font-size: 44px;
    line-height: 1.1;
    color: var(--ink);
  }
  .contact-list {
    position: absolute;
    left: 40px;
    top: 112px;
    list-style: none;
  }
  .contact-list__item {
    display: flex;
    align-items: center;
    gap: 9px;
    height: 27px;
    font-weight: 600;
    font-size: 15px;
    color: var(--ink);
  }
  .contact-list__icon {
    width: 14px;
    height: 14px;
    flex: none;
  }
</style>
</head>
<body>
  <main class="stage">
    <section class="card card--front" aria-label="Card front">
      <div class="card__band card__band--top"></div>
      <div class="card__jewellery" role="img" aria-label="Photograph of a gold chain necklace with a leaf pendant"></div>
      <div class="card__band card__band--bottom"></div>
      <h1 class="card__name">Clay Sparrow</h1>
    </section>

    <section class="card card--back" aria-label="Card back">
      <div class="card__band card__band--top"></div>
      <div class="card__jewellery" role="img" aria-label="Photograph of a gold chain necklace with a leaf pendant"></div>
      <div class="card__band card__band--bottom"></div>
      <ul class="contact-list">
        <li class="contact-list__item">
          <svg class="contact-list__icon" viewBox="0 0 14 14" aria-hidden="true">
            <path d="M3 1.5 L5 1 L6.2 4 L4.8 5.2 C5.6 7 7 8.4 8.8 9.2 L10 7.8 L13 9 L12.5 11 C12 12.3 10.5 12.8 9 12.2 C5.5 10.8 3.2 8.5 1.8 5 C1.2 3.5 1.7 2 3 1.5 Z" fill="var(--bark)"/>
          </svg>
          <span>0452867310</span>
        </li>
        <li class="contact-list__item">
          <svg class="contact-list__icon" viewBox="0 0 14 14" aria-hidden="true">
            <rect x="1" y="3" width="12" height="8.5" fill="var(--bark)"/>
            <path d="M1 3 L7 8 L13 3" fill="none" stroke="var(--kraft)" stroke-width="1.2"/>
          </svg>
          <span>sales@claysparrow-example.com.au</span>
        </li>
        <li class="contact-list__item">
          <svg class="contact-list__icon" viewBox="0 0 14 14" aria-hidden="true">
            <circle cx="7" cy="7" r="6" fill="var(--bark)"/>
            <path d="M1 7 H13 M7 1 C4.5 4 4.5 10 7 13 M7 1 C9.5 4 9.5 10 7 13" fill="none" stroke="var(--kraft)" stroke-width="1"/>
          </svg>
          <span>www.claysparrow-example.com.au</span>
        </li>
      </ul>
    </section>
  </main>
</body>
</html>
```